Stationery Design Project

Our business in mainly in the Natural Soap and Cosmetics.
Our letter heads, business cards and etc. to be have design on both side.

Target Market(s)

Aged from 21 to 60

Requirements
Must have
• Business card and Letter Head must have a chalkboard design on the back.

```html
<!DOCTYPE html>
<html lang="en">
<head>
<meta charset="utf-8">
<title>Lathery.co Stationery</title>
<link rel="stylesheet" href="https://fonts.googleapis.com/css2?family=Quicksand:wght@500&family=Crimson+Text&family=Josefin+Sans:wght@400&display=swap">
<style>
  :root {
    --backdrop: #e9e4dd;
    --chalk-dark: #2a2a2a;
    --chalk-mid: #363636;
    --chalk-line: #f2f2f2;
    --paper: #ffffff;
    --ink: #333333;
    --ink-soft: #555555;
    --leaf-tint: #e6e6e6;
  }
  * { box-sizing: border-box; margin: 0; padding: 0; }
  html, body { width: 1200px; height: 800px; overflow: hidden; }
  body { background: var(--backdrop); font-family: "Crimson Text", serif; color: var(--ink); position: relative; }

  .brand { font-family: "Quicksand", sans-serif; font-weight: 500; display: flex; align-items: center; gap: 6px; }
  .brand-dot { border-radius: 50%; background: currentColor; display: inline-block; }

  .hero-brand { position: absolute; left: 0; width: 1200px; top: 48px; justify-content: center; font-size: 24px; color: var(--ink); }
  .hero-brand .brand-dot { width: 12px; height: 12px; }

  .sheet { position: absolute; width: 384px; height: 544px; top: 150px; box-shadow: 0 2px 6px rgba(0,0,0,.18); }

  .letter-back { left: 40px; background: radial-gradient(ellipse at 40% 40%, var(--chalk-mid), var(--chalk-dark) 75%); color: var(--chalk-line); }
  .soap-diagram { position: absolute; left: 36px; top: 210px; width: 320px; height: 120px; border-radius: 4px; background: linear-gradient(180deg, rgba(255,255,255,.10), rgba(255,255,255,.04)); }
  .letter-back .brand { position: absolute; right: 22px; bottom: 22px; font-size: 13px; }
  .letter-back .brand-dot { width: 7px; height: 7px; }

  .letter-front { left: 444px; background: var(--paper); padding: 28px 30px 0 32px; }
  .letter-front .brand { position: absolute; right: 30px; top: 30px; font-size: 15px; color: var(--ink); }
  .letter-front .brand-dot { width: 8px; height: 8px; }
  .letter-body { margin-top: 104px; font-size: 7.6px; line-height: 1.42; text-align: justify; color: var(--ink-soft); }
  .letter-body p { margin-bottom: 9px; }
  .leaf-scatter { position: absolute; left: 40px; right: 80px; top: 396px; height: 124px; border-radius: 40px; background: radial-gradient(ellipse at center, var(--leaf-tint), rgba(230,230,230,0) 70%); }
  .letter-footer { position: absolute; left: 0; right: 0; bottom: 10px; text-align: center; font-family: "Josefin Sans", sans-serif; font-size: 5.6px; line-height: 1.5; color: var(--ink-soft); }

  .card { position: absolute; top: 150px; width: 108px; height: 160px; box-shadow: 0 2px 5px rgba(0,0,0,.18); }
  .card-front { left: 868px; background: var(--paper); text-align: center; padding-top: 40px; }
  .card-front .brand { justify-content: center; font-size: 13px; color: var(--ink); }
  .card-front .brand-dot { width: 7px; height: 7px; }
  .card-name { margin-top: 20px; font-family: "Josefin Sans", sans-serif; font-size: 9px; letter-spacing: .3px; }
  .card-rule { width: 60px; height: 1px; background: var(--ink); margin: 3px auto 4px; }
  .card-role { font-family: "Josefin Sans", sans-serif; font-size: 7px; }
  .card-contact { position: absolute; left: 0; right: 10px; bottom: 10px; text-align: right; font-family: "Josefin Sans", sans-serif; font-size: 5px; line-height: 1.5; }
  .card-back { left: 1000px; background: radial-gradient(ellipse at 40% 40%, var(--chalk-mid), var(--chalk-dark) 80%); color: var(--chalk-line); display: flex; align-items: center; justify-content: center; }
  .card-back .brand { font-size: 15px; }
  .card-back .brand-dot { width: 8px; height: 8px; }

  .app-screen { position: absolute; left: 868px; top: 470px; width: 100px; height: 168px; background: var(--paper); box-shadow: 0 2px 5px rgba(0,0,0,.18); display: flex; align-items: center; justify-content: center; }
  .app-screen .brand { font-size: 13px; color: var(--ink); }
  .app-screen .brand-dot { width: 7px; height: 7px; }
</style>
</head>
<body>
  <div class="brand hero-brand"><span class="brand-dot"></span>lathery.co</div>

  <section class="sheet letter-back">
    <div class="soap-diagram" role="img" aria-label="Chalk-drawn saponification diagram: fat or oil plus lye becomes fatty acid soap"></div>
    <div class="brand"><span class="brand-dot"></span>lathery.co</div>
  </section>

  <section class="sheet letter-front">
    <div class="brand"><span class="brand-dot"></span>lathery.co</div>
    <div class="letter-body">
      <p>Lorem ipsum dolor sit amet,</p>
      <p>Lorem ipsum dolor sit amet, consectetur adipiscing elit. Donec orci purus, luctus vitae dignissim eu, iaculis sed purus. Vivamus faucibus, ipsum nec aliquet viverra, leo mauris condimentum ligula, sit amet sagittis enim ligula quis arcu. Nam egestas tortor id nisi porttitor mattis. In tortor ante, ultricies in suscipit a, tempus non massa. Vivamus et auctor mi. Fusce vel massa nulla. Phasellus nec eros mauris, et scelerisque orci. Donec malesuada orci vitae nulla accumsan porta a id massa. Quisque accumsan iaculis magna sit amet fringilla. Maecenas consequat, magna eget tincidunt semper, odio nibh rutrum mi, id feugiat ante nisi eu risus. Vestibulum nunc orci, rhoncus a placerat in, ultricies in mi. Cras mattis varius eros, vel fringilla nisi suscipit eget.</p>
      <p>Quisque scelerisque sagittis nulla at porttitor. Mauris a justo et tellus interdum tristique. Sed id augue vitae urna euismod commodo aliquet a quam. Pellentesque arcu velit, cursus et malesuada ut, consequat et diam. Nullam erat sem, rhoncus id ullamcorper vitae, rhoncus et arcu. In ultricies ultricies nulla, ut rutrum nisi iaculis at. Donec eu magna a metus ornare faucibus. Fusce aliquet faucibus ultricies. Morbi semper, et id tincidunt gravida, sem arcu adipiscing lacus, ac bibendum nulla leo eu purus. Quisque nec diam sed risus consectetur a cumsan quis quis nibh. Vestibulum id purus lorem.</p>
      <p>Vivamus vehicula accumsan lacinia. Aliquam erat volutpat. Pellentesque consequat venenatis velit non gravida. Etiam et sem et nulla congue aliquam sed eget augue. Nulla facilisi. Pellentesque habitant morbi tristique senectus et netus et malesuada fames ac turpis egestas. Nulla a elit at sem iaculis congue. Nullam mollis tristique lobortis.</p>
    </div>
    <div class="leaf-scatter" role="img" aria-label="Faint scattered leaf and petal illustration"></div>
    <div class="letter-footer">LATHERY.CO - Natural Soap and Cosmetics<br>Tel. (000) 555-0187 &bull; hello@lathery.co &bull; website: lathery.co</div>
  </section>

  <section class="card card-front">
    <div class="brand"><span class="brand-dot"></span>lathery.co</div>
    <div class="card-name">ROWAN HALE</div>
    <div class="card-rule"></div>
    <div class="card-role">CEO</div>
    <div class="card-contact">(000) 555-0187<br>rowan@lathery.co<br>lathery.co</div>
  </section>

  <section class="card card-back">
    <div class="brand"><span class="brand-dot"></span>lathery.co</div>
  </section>

  <section class="app-screen">
    <div class="brand"><span class="brand-dot"></span>lathery.co</div>
  </section>
</body>
</html>
```